Vernalis Medical Business Card

Create a high class Business card for Medical Aesthetics and Wellness Practice called Vernalis Medical Aesthetics and Wellness as per the logo attached.
Addresss is: 412 Harlow Brook Road Suite 318 Melville, New York 11583
Phone (516)294-7051 IG @vernalis_medical
Vernalismedical-example.com

I need 5 different name configurations
1) Dr. Derek Haltsworth
Aesthetics and Wellness Specialist
Medical Director

2) Rosalind Petrakova, NP
Clinical Nurse Manager

3) Maren Culbrith, RN
Aesthetic Nurse Specialist

4) Talia Verhoeven, RN

5) Dana Ostrowe, L.E.
Senior Licensed Esthetician

Target Market(s)

22-55 Females

Industry/Entity Type

Medical Spa and Wellness

Contact Information for Business Card

Logo, address, phone, web, instagram, providers name

Requirements
Must have
• Attractive classy modern look

```html
<!DOCTYPE html>
<html lang="en">
<head>
<meta charset="utf-8">
<title>Vernalis Medical Business Card</title>
<link rel="stylesheet" href="https://fonts.googleapis.com/css2?family=Cormorant+Garamond:wght@500&family=Arimo:wght@400;700&display=swap">
<style>
  :root{
    --stage:#151515;
    --paper:#f6f5f0;
    --teal:#0f3d4c;
    --ink:#3c3c3c;
    --rule:#555;
    --dash:#a9a9a9;
  }
  *{box-sizing:border-box;margin:0;padding:0}
  html,body{width:1200px;height:963px;overflow:hidden;background:var(--stage)}
  .canvas{position:relative;width:1200px;height:963px}
  .card{position:absolute;left:250px;width:700px;height:400px;background:var(--paper);overflow:hidden}
  .card--front{top:40px}
  .card--back{top:523px}

  .brand{position:absolute;text-align:center;font-family:"Cormorant Garamond",serif;font-weight:500;color:var(--teal)}
  .brand__name{font-size:64px;line-height:1;letter-spacing:2px}
  .brand__tag{font-size:17px;font-variant:small-caps;letter-spacing:1px;margin-top:6px}
  .brand__city{font-size:11px;letter-spacing:7px;text-transform:uppercase;margin-top:4px}
  .card--front .brand{left:330px;top:80px;width:340px}
  .card--back .brand{left:0;top:28px;width:700px;color:var(--paper)}

  .person{position:absolute;left:40px;top:100px;font-family:Arimo,sans-serif;color:var(--ink);font-size:14px;line-height:1.3}
  .person__name{font-family:"Cormorant Garamond",serif;font-weight:500;font-variant:small-caps;color:var(--teal);font-size:26px;letter-spacing:.5px;line-height:1.1;margin-bottom:2px}
  .divider{position:absolute;left:30px;top:200px;width:640px;height:1px;background:var(--rule)}
  .contact{position:absolute;left:40px;top:214px;list-style:none;font-family:Arimo,sans-serif;color:var(--ink);font-size:14px;line-height:1.55}
  .contact li{display:flex;align-items:center;gap:7px}
  .contact svg{width:12px;height:12px;flex:none}
  .address{position:absolute;right:40px;top:292px;text-align:right;font-family:Arimo,sans-serif;color:var(--ink);font-size:14px;line-height:1.4}
  .front-band{position:absolute;left:0;bottom:0;width:100%;height:22px;background:var(--teal)}

  .back-band{position:absolute;left:0;top:0}
  .appointment{position:absolute;left:0;top:190px;width:700px;text-align:center;font-family:Arimo,sans-serif;font-weight:700;color:var(--paper);font-size:19px;letter-spacing:1px}
  .note-line{position:absolute;left:40px;width:620px;border-top:1px dashed var(--dash)}
  .field{position:absolute;top:352px;display:flex;align-items:flex-end;gap:8px;font-family:Arimo,sans-serif;color:var(--ink);font-size:14px}
  .field span.line{display:block;height:1px;background:var(--rule);margin-bottom:3px}
</style>
</head>
<body>
<main class="canvas">

  <section class="card card--front" aria-label="Business card front">
    <div class="brand">
      <div class="brand__name">Vernalis</div>
      <div class="brand__tag">Medical Aesthetics and Wellness</div>
      <div class="brand__city">New York</div>
    </div>

    <div class="person">
      <div class="person__name">Dr. Derek Haltsworth</div>
      <div>Aesthetics and Wellness Specialist</div>
      <div>Medical Director</div>
    </div>

    <div class="divider"></div>

    <ul class="contact">
      <li><svg viewBox="0 0 12 12"><path fill="#3c3c3c" d="M2.5 1l2 2.2-1 1.2c.7 1.5 1.8 2.6 3.3 3.3l1.2-1 2.2 2-1 2C5.2 10.5 1.5 6.8 1 2.2z"/></svg>(516)294-7051 IG</li>
      <li><svg viewBox="0 0 12 12"><circle cx="6" cy="6" r="5" fill="#3c3c3c"/></svg>@vernalis_medical</li>
      <li><svg viewBox="0 0 12 12"><circle cx="6" cy="6" r="5" fill="none" stroke="#3c3c3c" stroke-width="1.3"/><path d="M1 6h10M6 1c-2.5 3-2.5 7 0 10M6 1c2.5 3 2.5 7 0 10" fill="none" stroke="#3c3c3c" stroke-width="1"/></svg>Vernalismedical-example.com</li>
    </ul>

    <div class="address">
      412 Harlow Brook Road<br>
      Suite 318<br>
      Melville, New York 11583
    </div>

    <div class="front-band"></div>
  </section>

  <section class="card card--back" aria-label="Appointment card back">
    <svg class="back-band" width="700" height="240" viewBox="0 0 700 240">
      <rect x="0" y="0" width="700" height="170" fill="var(--teal)"/>
      <rect x="0" y="176" width="700" height="4" fill="var(--teal)"/>
      <path d="M150 180H560V226L520 232H190L150 226Z" fill="var(--teal)"/>
    </svg>
    <div class="brand">
      <div class="brand__name">Vernalis</div>
      <div class="brand__tag">Medical Aesthetics and Wellness</div>
      <div class="brand__city">New York</div>
    </div>
    <div class="appointment">APPOINTMENT</div>

    <div class="note-line" style="top:272px"></div>
    <div class="note-line" style="top:308px"></div>

    <div class="field" style="left:40px">DATE <span class="line" style="width:290px"></span></div>
    <div class="field" style="left:390px">TIME <span class="line" style="width:230px"></span></div>
  </section>

</main>
</body>
</html>
```